【10枚一括】接骨院の手書きポスターデザインをベクターデータ化(活字化・トレース)依頼 【依頼の目的】 院内ポスターを印刷会社で繰り返し印刷するため、データをベクターデータ(AI形式)にしたい。 【依頼内容】添付した10枚の手書きポスターをベクターデータ化(トレース)してください。 コンペで提出は添付が画像の②の作成をお願いいたします。 【ご依頼事項】 1. イラスト・見出し文字: 手書きの風合いを残しつつ、拡大してもシャープな線になるようトレースをお願いします。 2. 本文(小さい文字): 視認性向上のため、手書きのままトレースせず、読みやすいフォントに打ち直して配置を整えてください。 文言の多少の変更、ロゴデータの挿入等契約後にご相談させていただきます。 【納品形式】Adobe Illustrator形式(AIデータ)、カラーモードはCMYKでお願いします。 【希望サイズ】最終的にA2〜A1サイズで印刷予定です。実寸で350dpi以上の解像度で作成をお願いします。 【納期】2026年1月20日 【予算(固定報酬)】10万円 ※契約金額(税込)からシステム利用料を差し引いた金額が、ワーカーさまの受取金額となります その他ご質問等ありましたら、気軽にお問い合わせください。 ご応募をお待ちしております! |
画質の綺麗さ、すっきりして一番見やすかったため今回採用させていただきました。
皆さまご提案ありがとうございました。短い期間の中多数のご応募いただきありがとうございます。
今後も機会があれば依頼させていただきますのでよろしくお願いいたします。

```html
<!DOCTYPE html>
<html lang="ja">
<head>
<meta charset="utf-8">
<title>当院のイチオシMENU</title>
<link href="https://fonts.googleapis.com/css2?family=Dela+Gothic+One&family=Zen+Maru+Gothic:wght@700;900&display=swap" rel="stylesheet">
<style>
  :root {
    --cream: #fdf6c9;
    --ink: #1a1a1a;
    --accent-red: #e0262d;
    --c-red: #d9262f;
    --c-pink: #ee9fba;
    --c-lightpink: #f4b7c9;
    --c-orange: #f08a24;
    --c-blue: #2369b5;
    --c-sky: #56b4e6;
    --c-green: #6cb83a;
    --c-yellow: #f6c500;
    --white: #ffffff;
    --leaf: #8cc63f;
  }
  * { box-sizing: border-box; margin: 0; padding: 0; }
  html, body { width: 1200px; height: 848px; overflow: hidden; background: var(--cream); }
  .poster { position: relative; width: 1200px; height: 848px; background: var(--cream); color: var(--ink); }

  .headline {
    position: absolute; left: 0; top: 26px; width: 1200px; text-align: center;
    font-family: "Dela Gothic One", sans-serif; font-weight: 400; font-size: 92px; line-height: 1;
    letter-spacing: 2px; white-space: nowrap;
  }
  .headline-bar {
    position: absolute; left: 22px; top: 140px; width: 1156px; height: 16px;
    background: var(--accent-red); border-radius: 8px; transform: rotate(-0.4deg);
  }

  .menu-card {
    position: absolute; width: 272px; height: 258px; border-radius: 16px; padding: 10px;
  }
  .menu-card .panel {
    position: relative; width: 100%; height: 100%; background: var(--white); border-radius: 8px;
    overflow: hidden;
  }
  .bubble {
    position: absolute; left: 12px; top: 6px; width: 228px; height: 96px;
    border: 3px solid var(--ink); border-radius: 50%; background: var(--white);
    display: flex; flex-direction: column; align-items: center; justify-content: center;
    font-family: "Zen Maru Gothic", sans-serif; font-weight: 900; font-size: 17px; line-height: 1.3;
    text-align: center; white-space: nowrap;
  }
  .bubble::after {
    content: ""; position: absolute; left: 48px; bottom: -14px; width: 18px; height: 18px;
    background: var(--white); border-right: 3px solid var(--ink); border-bottom: 3px solid var(--ink);
    transform: skewX(30deg) rotate(20deg);
  }
  .bubble .big { font-size: 22px; }
  .bubble .small { font-size: 13px; }
  .mark { border-bottom: 4px solid var(--accent-red); padding: 0 2px; }
  .menu-name {
    position: absolute; left: 0; top: 0; width: 100%; height: 100%;
    display: flex; align-items: center; justify-content: center; padding-top: 68px;
    font-family: "Dela Gothic One", sans-serif; font-weight: 400; font-size: 42px; line-height: 1;
    white-space: nowrap; text-align: center;
  }
  .menu-name.long { font-size: 36px; }
  .menu-name.xlong { font-size: 32px; letter-spacing: -1px; }
  .leaf-strip {
    position: absolute; left: 14px; right: 14px; bottom: 14px; height: 10px;
    background: repeating-linear-gradient(90deg, var(--leaf) 0 8px, transparent 8px 18px);
    border-radius: 4px;
  }

  .r1 { top: 204px; } .r2 { top: 498px; }
  .k1 { left: 24px; } .k2 { left: 316px; } .k3 { left: 608px; } .k4 { left: 900px; }

  .footer-note {
    position: absolute; left: 30px; top: 778px;
    font-family: "Zen Maru Gothic", sans-serif; font-weight: 900; font-size: 27px; white-space: nowrap;
  }
  .clinic-name {
    position: absolute; right: 34px; top: 770px; text-align: center;
    font-family: "Zen Maru Gothic", sans-serif; font-weight: 900; line-height: 1.2; white-space: nowrap;
  }
  .clinic-name .sub { font-size: 12px; display: block; }
  .clinic-name .main { font-size: 24px; display: block; }
</style>
</head>
<body>
<main class="poster">
  <h1 class="headline">当院のイチオシMENU!!</h1>
  <div class="headline-bar"></div>

  <section class="menu-card r1 k1" style="background:var(--c-red)">
    <div class="panel">
      <div class="menu-name">骨盤矯正</div>
      <div class="bubble"><span>姿勢や骨盤の</span><span><span class="mark">歪みが気になる方へ</span></span></div>
      <div class="leaf-strip" role="img" aria-label="小さな葉の飾り模様"></div>
    </div>
  </section>

  <section class="menu-card r1 k2" style="background:var(--c-pink)">
    <div class="panel">
      <div class="menu-name long">産後骨盤矯正</div>
      <div class="bubble"><span><span class="mark">産後の不調</span></span><span>悩んでませんか？</span></div>
      <div class="leaf-strip" role="img" aria-label="小さな葉の飾り模様"></div>
    </div>
  </section>

  <section class="menu-card r1 k3" style="background:var(--c-lightpink)">
    <div class="panel">
      <div class="menu-name">EMS</div>
      <div class="bubble"><span><span class="mark">インナーマッスル</span></span><span>鍛えます！！</span></div>
      <div class="leaf-strip" role="img" aria-label="小さな葉の飾り模様"></div>
    </div>
  </section>

  <section class="menu-card r1 k4" style="background:var(--c-orange)">
    <div class="panel">
      <div class="menu-name long">交通事故治療</div>
      <div class="bubble"><span class="small">むちうちなどの</span><span class="big"><span class="mark">後遺症</span></span><span class="small">放っておくと長引くかも?!</span></div>
      <div class="leaf-strip" role="img" aria-label="小さな葉の飾り模様"></div>
    </div>
  </section>

  <section class="menu-card r2 k1" style="background:var(--c-blue)">
    <div class="panel">
      <div class="menu-name">猫背矯正</div>
      <div class="bubble"><span>まあるい背中</span><span><span class="mark">伸ばしましょう!!</span></span></div>
      <div class="leaf-strip" role="img" aria-label="小さな葉の飾り模様"></div>
    </div>
  </section>

  <section class="menu-card r2 k2" style="background:var(--c-sky)">
    <div class="panel">
      <div class="menu-name xlong">ハイボルテージ</div>
      <div class="bubble"><span>急な痛みを</span><span class="big"><span class="mark">一発改善!!</span></span></div>
      <div class="leaf-strip" role="img" aria-label="小さな葉の飾り模様"></div>
    </div>
  </section>

  <section class="menu-card r2 k3" style="background:var(--c-green)">
    <div class="panel">
      <div class="menu-name long">はり・きゅう</div>
      <div class="bubble"><span class="big">慢性痛…</span><span class="big"><span class="mark">体質改善</span></span><span class="small">してみませんか？</span></div>
      <div class="leaf-strip" role="img" aria-label="小さな葉の飾り模様"></div>
    </div>
  </section>

  <section class="menu-card r2 k4" style="background:var(--c-yellow)">
    <div class="panel">
      <div class="menu-name long">トリガーMA</div>
      <div class="bubble"><span><span class="mark">痛みの原因</span>に</span><span>マッサージ!!</span></div>
      <div class="leaf-strip" role="img" aria-label="小さな葉の飾り模様"></div>
    </div>
  </section>

  <p class="footer-note">★患者様それぞれに合った治療メニューをご提案いたします!!</p>
  <div class="clinic-name"><span class="sub">ひかり鍼灸接骨院</span><span class="main">若葉台院</span></div>
</main>
</body>
</html>
```